Q spot menu

single page
we are located right across from Larkfield Grounds Gullwings ballpark
Menu has to be double sided 11”x17”

APPETIZERS
Guacamole and Chips $14 HH $9
House-made guacamole and tortilla chips. Served with pico de gallo, queso fresco and salsa.

Grand Slam Nachos $18 HH $13
House-made tortilla chips smothered with Jack and cheddar cheeses, your choice of meat (seasoned ground beef, chicken, pork carnitas, or veggies, beans, and jalapeños. Served with sour cream, guacamole, pico de gallo and salsa.

Quesadilla 15 HH$10
Flour tortilla filled with Jack and cheddar cheeses, your choice of meat (seasoned ground beef, chicken, pork carnitas, or veggies. folded in half and cooked golden brown. Served with sour cream and guacamole.

Beef Sliders $15
Premium Angus beef, Jack cheese, sauteed onions, rajas, tomato, spring mix, house mayo and chipotle aioli on a brioche bun.

Chicken Strips $15 HH $10
House-battered and breaded chicken breast strips. Served with your choice of dressing and fries. SUB ONION RINGS +$3

Corvo Wings $15 HH $10
7 Jumbo-size drums and flats tossed in your choice of sauce (BBQ, buffalo, mango habanero, or lemon pepper) or dry. Served with carrots, celery sticks, and your choice of dressing.

Onion Rings $9
Jumbo onion rings. Served with your choice of dressing.

Mozzarella Sticks $10
7 Breaded and fried mozzarella cheese sticks. Served with marinara sauce and ranch dressing.

SALADS
All salads are served with your choice of dressing (Ranch, Blue cheese, Honey mustard, or Balsamic vinaigrette).

Dinner Salad $9
Mixed greens, tomatoes, onions, cheese and carrots.

Taco Salad $17
Large flour tortilla crispy shell filled with your choice of meat (seasoned ground beef, pork carnitas, chicken or veggies, beans, lettuce, tomatoes, jalapeños and cheese. Topped with sour cream, pico de gallo and salsa.

Ahi Tuna Salad $19
Pan-seared Ahi tuna steak (6 oz.) on a bed of spring mix, tomatoes, beets, orange slices and sesame seeds.

Salmon Salad $20
Pan-seared salmon filet, on a bed of mixed greens, tomatoes, onions, avocado slices, carrots and cheese.
BURGERS ( 8oz)
Served with fries. (add an egg +$2)
El Gran Tio Burger $17
Verified Prairie Stock patty, cheddar cheese, and caramelized onions, mayo, lettuce, tomato, avocado and a fried jalapeño.

All-American Burger $16
Verified Prairie Stock patty, Cheddar cheese, mayo, lettuce, tomato, onion and pickles.
- Add bacon +$3
- Add an egg +$2

Whiskey Burger $17
Verified Prairie Stock patty, bacon, caramelized onions and Swiss cheese, mayo and house-made Moss Haverty whiskey sauce.

Mushroom Swiss Burger $17
Verified Prairie Stock patty, mayo, Swiss cheese, bacon, and mushrooms on ciabatta bread.

Veggie Burger $16 (VG)
Black bean patty on a pretzel bun with mayo, lettuce, tomato, onion, pickles, and avocado.

Salmon Burger $17
Pan-seared salmon filet (6 oz.) on a pretzel bun with mayo, lettuce, tomato, avocado and chipotle aioli.

Grilled Chicken Sandwich $16
Mayo, grilled chicken breast on ciabatta bread with lettuce, tomato, onions, pickles, and avocado.

SOUTH OF THE BORDER
3 Street Tacos 12 HH $7
seasoned ground beef, pork carnitas, chicken or veggies, pico de gallo and salsa. ADD GUAC +$3

2-lb. Burrito $15
Flour tortilla wrapped around your choice of meat seasoned ground beef, pork, chicken, or veggies. rice, beans, guacamole, sour cream, salsa and Jack and cheddar cheeses.

Chile Colorado Burrito $16
Special Trim Beef simmered in a house-made Chile Colorado sauce, rice and beans wrapped in a flour tortilla. Topped with sour cream.

EVENT MENU
Grand Slam Nachos $18
House-made tortilla chips smothered with Jack and cheddar cheeses, your choice of meat (seasoned ground beef, pork, chicken or veggies. beans and jalapeños. Served with sour cream, guacamole, pico de gallo and salsa.

3 Street Tacos $12
Your choice of meat seasoned ground beef, pork carnitas, chicken, or veggies, pico de gallo and salsa.

2-lb. Burrito $15
Flour tortilla wrapped around your choice of meat (seasoned ground beef, pork carnitas or grilled chicken) or veggies, rice, beans, guacamole, sour cream, salsa and Jack and cheddar cheeses.

Quesadilla $15
Flour tortilla filled with Jack and cheddar cheeses, your choice of meat (seasoned ground beef, pork carnitas, chicken or veggies, folded in half and cooked golden brown. Served with guacamole, pico de gallo and sour cream.

Taco Salad $17

Corvo Wings $15
7 Jumbo-size drums and flats tossed in your choice of sauce (BBQ, buffalo, mango habanero, or lemon pepper) or dry. Served with carrot and celery sticks.

Chicken Strips $15
House-battered and breaded chicken breast strips. Served with fries and your choice dressing.

All-American Burger $16
Verified Prairie Stock patty, Cheddar cheese, with mayo, lettuce, tomato, onion and pickles.
- Add bacon +$3
- Add avocado +$3

Whiskey Burger $17
Verified Prairie Stock patty, bacon, caramelized onions and Swiss cheese, with mayo and house-made Moss Haverty whiskey sauce.

Veggie Burger $16
Black bean patty, with mayo, lettuce, tomato, onion, pickles and avocado.

SIDES
basket of French fries $7
Rice $5
Beans $5
Sour cream $1
Avocado $4
Guacamole $7
Salsa 4oz. $2
Dressing $1

HOUSE SPECIALTIES
Carne Asada Entrée $23
Charbroiled skirt steak, cooked to order. Served with rice, beans, pico de gallo, salsa, sour cream, guacamole and tortillas.

Chile Colorado Entrée $18
Special Trim Beef simmered in a house-made Chile Colorado sauce. Served with rice, beans, sour cream and tortillas.

Pork Shank (Wednesdays only, until sold out) $24
Slow-baked pork shank (fork tender and fall-off-the-bone moist). Served with rice, beans, pico de gallo, salsa and tortillas. Ask your server about availability.

BEVERAGES
Soft Drinks $3.50
Zolta, Diet Zolta, Brook Fizz,
Juice $5
Orange, cranberry, pineapple, grapefruit
Milk $4

HAPPY HOUR
Mon- Fri 2-5pm & 10-Close
Any draft beer $2 off
Selected appetizers $5 off
Well drinks $2 off
Wine $2 off

Daily specials 11:30 am - 5 pm

Margarita Monday $2 off /Burgers 20%off
Tacos Tuesday $5 off /Tequila Casa Verano 1871 $19.42
Wing Wednesday $5 Off / whiskey $2 Off
Thirsty Thursday Any draft beer $5/Nachos $5 off
Emberloch Friday $6 shot /Chile colorado burrito 20%off
Saturday and Sunday Brunch 10am-1pm. Mimosas and Bloody Marrys

Please make sure that you put this note on both pages * *CONSUMING RAW OR UNDERCOOKED MEATS, POULTRY, SEAFOOD, SHELLFISH, OR EGGS MAY INCREASE YOUR RISK OF FOODBORNE ILLNESS, ESPECIALLY IF YOU HAVE CERTAIN MEDICAL CONDITIONS.

Items that have eggs or meet HAS TO BE MARKED WITH AN ASTERISK*

AUTOMATIC 20% GRATUITY ON GROUPS OF 5 OR MORE. ALL ORDERS TO GO +$1

Target Market(s)

Young crowd

Industry/Entity Type

Sports bar

Colors
FFC000
F8CF3A
FAE287
FDF2CF
FEFAEE

Requirements
Must have
• Entire menu
Nice to have
• Menu has to be simple bat VERY attractive

```html
<!DOCTYPE html>
<html lang="en">
<head>
<meta charset="utf-8">
<title>Q spot menu</title>
<link href="https://fonts.googleapis.com/css2?family=Bungee&family=Montserrat:ital,wght@0,400;0,500;0,700;1,500;1,700&display=swap" rel="stylesheet">
<style>
:root{
  --gold:#FFC000;
  --sun:#F8CF3A;
  --butter:#FAE287;
  --cream:#FDF2CF;
  --ivory:#FEFAEE;
  --orange:#F26B0F;
  --deep:#EE5A0A;
  --panel:rgba(248,207,58,.82);
}
*{box-sizing:border-box;margin:0;padding:0}
html,body{width:776px;height:1200px;overflow:hidden}
body{
  position:relative;
  font-family:"Montserrat",sans-serif;
  color:var(--orange);
  background:radial-gradient(circle at 50% 30%,#FFD84A 0%,var(--gold) 70%,#FDB300 100%);
}
.panel{position:absolute;background:var(--panel);border-radius:6px;overflow:hidden}
.photo{position:absolute;left:0;right:0;top:0}
.photo.top{height:150px;background:linear-gradient(180deg,#d9c9a8 0%,#c89a55 50%,rgba(248,207,58,0) 100%)}
.photo.salad{background:linear-gradient(180deg,#b9a276 0%,#8fae4e 50%,rgba(248,207,58,0) 100%)}
.photo.event{background:linear-gradient(180deg,#8a8478 0%,#c23b1f 50%,rgba(248,207,58,0) 100%)}
.photo.nachos{height:140px;background:linear-gradient(180deg,#e8d9a8 0%,#c9a24a 50%,rgba(248,207,58,0) 100%)}
.photo.fries{top:auto;bottom:0;height:110px;background:linear-gradient(0deg,#c9a046 0%,#b07a38 40%,rgba(248,207,58,0) 100%)}
.burger-photo{position:absolute;left:394px;top:397px;width:157px;height:154px;border-radius:46% 46% 40% 40%;background:radial-gradient(circle at 50% 40%,#e9a23a 0%,#8a3c1b 55%,rgba(138,60,27,0) 72%)}
.content{position:absolute}
.heading{font-family:"Bungee",sans-serif;font-size:19px;letter-spacing:1px;color:var(--deep);line-height:1}
.heading.center{text-align:center}
.item{margin-top:12px}
.tight .item{margin-top:9px}
.name{font-weight:700;font-size:8px;letter-spacing:.6px;text-transform:uppercase;line-height:1.25}
.name span{font-weight:400}
.desc{font-size:6.3px;text-transform:uppercase;line-height:9px;letter-spacing:.1px}
.desc em{display:block;font-style:italic}
.note{font-size:6.3px;text-transform:uppercase;line-height:8px;text-align:center}
.sides{display:flex;gap:8px;align-items:center}
.sides-label{writing-mode:vertical-rl;transform:rotate(180deg);font-family:"Bungee",sans-serif;font-size:11px}
.sides-grid{display:grid;grid-template-columns:93px 70px;font-size:6.3px;font-style:italic;font-weight:500;text-transform:uppercase;line-height:9px}
.specialties{position:absolute;left:278px;top:921px;width:455px;height:127px;background:var(--deep);border-radius:6px;color:var(--butter)}
.specialties-title{font-family:"Bungee",sans-serif;font-size:18px;line-height:1.05;color:var(--deep);-webkit-text-stroke:1px var(--butter);letter-spacing:.5px}
.happy{position:absolute;left:46px;top:1014px;width:222px;text-align:center;color:var(--deep)}
.happy-title{font-family:"Bungee",sans-serif;font-size:27px;line-height:1;color:var(--butter);-webkit-text-stroke:1.3px var(--deep)}
.happy p{font-family:"Bungee",sans-serif;font-size:11.5px;line-height:13px;color:var(--deep)}
.happy .o{color:var(--butter);-webkit-text-stroke:.9px var(--deep)}
.daily-bar{position:absolute;left:46px;top:1164px;width:222px;height:40px;background:var(--deep);border-radius:6px 6px 0 0;color:var(--cream);font-size:11.5px;text-align:center;padding-top:11px;letter-spacing:.3px}
.beverages{position:absolute;left:283px;top:1058px;width:450px;display:flex;gap:16px}
.bev-title{font-family:"Bungee",sans-serif;font-size:18px;color:var(--deep);line-height:1}
.bev{font-size:9px;font-style:italic;font-weight:500;text-transform:uppercase;line-height:1.1}
.days{position:absolute;left:285px;top:1103px;width:450px;font-size:9.3px;font-weight:700;text-transform:uppercase;line-height:9.9px;color:var(--deep)}
.days span{font-weight:500;font-style:italic}
.disclaimer{position:absolute;left:285px;top:1170px;width:450px;font-size:6.2px;font-style:italic;text-transform:uppercase;line-height:1.3;color:#f08a2a}
</style>
</head>
<body>

<section class="panel" style="left:46px;top:50px;width:222px;height:606px">
  <div class="photo top" role="img" aria-label="Photo of a cut quesadilla with guacamole"></div>
  <div class="content" style="left:26px;top:118px;width:178px">
    <h2 class="heading center" style="margin-left:-10px">APPETIZERS</h2>
    <div class="item" style="margin-top:12px"><p class="name">Guacamole and Chips <span>$14 HH $9</span></p><p class="desc">House-made guacamole and tortilla chips. Served with pico de gallo, queso fresco and salsa.</p></div>
    <div class="item"><p class="name">Grand Slam Nachos <span>$18 HH $13</span></p><p class="desc">House-made tortilla chips smothered with Jack and cheddar cheeses, your choice of meat (seasoned ground beef, chicken, pork carnitas, or veggies, beans, and jalapeños. Served with sour cream, guacamole, pico de gallo and salsa.</p></div>
    <div class="item"><p class="name">Quesadilla <span>$15 HH $10</span></p><p class="desc">Flour tortilla filled with Jack and cheddar cheeses, your choice of meat (seasoned ground beef, chicken, pork carnitas, or veggies. Folded in half and cooked golden brown. Served with sour cream and guacamole.</p></div>
    <div class="item"><p class="name">Beef Sliders <span>$15</span></p><p class="desc">Premium Angus beef, Jack cheese, sauteed onions, rajas, tomato, spring mix, house mayo and chipotle aioli on a brioche bun.</p></div>
    <div class="item"><p class="name">Chicken Strips <span>$15 HH $10</span></p><p class="desc">House-battered and breaded chicken breast strips. Served with your choice of dressing and fries. Sub onion rings +$3</p></div>
    <div class="item"><p class="name">Corvo Wings <span>$15 HH $10</span></p><p class="desc">7 jumbo-size drums and flats tossed in your choice of sauce (BBQ, buffalo, mango habanero, or lemon pepper) or dry. Served with carrots, celery sticks, and your choice of dressing.</p></div>
    <div class="item"><p class="name">Onion Rings <span>$9</span></p><p class="desc">Jumbo onion rings. Served with your choice of dressing.</p></div>
    <div class="item"><p class="name">Mozzarella Sticks <span>$10</span></p><p class="desc">7 breaded and fried mozzarella cheese sticks. Served with marinara sauce and ranch dressing.</p></div>
  </div>
</section>

<section class="panel" style="left:278px;top:50px;width:221px;height:405px">
  <div class="photo top salad" role="img" aria-label="Photo of a taco salad in a crispy tortilla shell"></div>
  <div class="content" style="left:26px;top:118px;width:172px">
    <h2 class="heading center">SALADS</h2>
    <p class="note" style="margin-top:10px">All salads are served with your choice of dressing (Ranch, Blue cheese, Honey mustard, or Balsamic vinaigrette).</p>
    <div class="item" style="margin-top:9px"><p class="name">Dinner Salad <span>$9</span></p><p class="desc">Mixed greens, tomatoes, onions, cheese and carrots.</p></div>
    <div class="item"><p class="name">Taco Salad <span>$17</span></p><p class="desc">Large flour tortilla crispy shell filled with your choice of meat (seasoned ground beef, pork carnitas, chicken or veggies, beans, lettuce, tomatoes, jalapeños and cheese. Topped with sour cream, pico de gallo and salsa.</p></div>
    <div class="item"><p class="name">Ahi Tuna Salad <span>$19</span></p><p class="desc">Pan-seared ahi tuna steak (6 oz.) on a bed of spring mix, tomatoes, beets, orange slices and sesame seeds.</p></div>
    <div class="item"><p class="name">Salmon Salad <span>$20</span></p><p class="desc" style="width:96px">Pan-seared salmon filet, on a bed of mixed greens, tomatoes, onions, avocado slices, carrots and cheese.</p></div>
  </div>
</section>

<section class="panel" style="left:278px;top:465px;width:221px;height:448px">
  <div class="photo fries" role="img" aria-label="Photo of a grilled chicken sandwich with fries"></div>
  <div class="content" style="left:26px;top:22px;width:180px">
    <h2 class="heading">BURGER</h2>
    <p class="desc" style="margin-top:4px;width:80px;line-height:7.5px">(8oz)<br>Served with fries<br>(add an egg +$2)</p>
    <div class="item" style="margin-top:10px"><p class="name">El Gran Tio<br>Burger <span>$17</span></p><p class="desc" style="width:165px">Verified Prairie Stock patty, cheddar cheese, and caramelized onions, mayo, lettuce, tomato, avocado and a fried jalapeño.</p></div>
    <div class="item" style="margin-top:10px"><p class="name">All-American Burger <span>$16</span></p><p class="desc">Verified Prairie Stock patty, cheddar cheese, mayo, lettuce, tomato, onion and pickles.<em>- Add bacon +$3</em><em>- Add an egg +$2</em></p></div>
    <div class="item" style="margin-top:10px"><p class="name">Whiskey Burger <span>$17</span></p><p class="desc">Verified Prairie Stock patty, bacon, caramelized onions and Swiss cheese, mayo and house-made Moss Haverty whiskey sauce.</p></div>
    <div class="item" style="margin-top:10px"><p class="name">Mushroom Swiss Burger <span>$17</span></p><p class="desc">Verified Prairie Stock patty, mayo, Swiss cheese, bacon, and mushrooms on ciabatta bread.</p></div>
    <div class="item" style="margin-top:10px"><p class="name">Veggie Burger <span>$16</span></p><p class="desc">Black bean patty on a pretzel bun with mayo, lettuce, tomato, onion, pickles, and avocado.</p></div>
    <div class="item" style="margin-top:10px"><p class="name">Salmon Burger <span>$17</span></p><p class="desc">Pan-seared salmon filet (6 oz.) on a pretzel bun with mayo, lettuce, tomato, avocado and chipotle aioli.</p></div>
    <div class="item" style="margin-top:10px"><p class="name">Grilled Chicken Sandwich <span>$16</span></p><p class="desc">Mayo, grilled chicken breast on ciabatta bread with lettuce, tomato, onions.</p></div>
  </div>
</section>

<div class="burger-photo" role="img" aria-label="Photo of a burger with a fried egg on a pretzel bun"></div>

<section class="panel tight" style="left:510px;top:50px;width:221px;height:863px">
  <div class="photo top event" role="img" aria-label="Photo of a burrito topped with red sauce and sour cream"></div>
  <div class="content" style="left:26px;top:118px;width:174px">
    <h2 class="heading center" style="margin-left:-12px">EVENT MENU</h2>
    <div class="item" style="margin-top:12px"><p class="name">Grand Slam Nachos <span>$18</span></p><p class="desc">House-made tortilla chips smothered with Jack and cheddar cheeses, your choice of meat (seasoned ground beef, pork, chicken or veggies. Beans and jalapeños. Served with sour cream, guacamole, pico de gallo and salsa.</p></div>
    <div class="item"><p class="name">3 Street Tacos <span>$12</span></p><p class="desc">Your choice of meat seasoned ground beef, pork carnitas, chicken, or veggies, pico de gallo and salsa.</p></div>
    <div class="item"><p class="name">2-lb. Burrito <span>$15</span></p><p class="desc">Flour tortilla wrapped around your choice of meat (seasoned ground beef, pork carnitas or grilled chicken) or veggies, rice, beans, guacamole, sour cream, salsa and Jack and cheddar cheeses.</p></div>
    <div class="item"><p class="name">Quesadilla <span>$15</span></p><p class="desc">Flour tortilla filled with Jack and cheddar cheeses, your choice of meat (seasoned ground beef, pork carnitas, chicken or veggies, folded in half and cooked golden brown. Served with guacamole, pico de gallo and sour cream.</p></div>
    <div class="item"><p class="name">Taco Salad <span>$17</span></p><p class="desc">Large flour tortilla crispy shell filled with your choice of meat (seasoned ground beef, pork carnitas, chicken or veggies, beans, lettuce, tomatoes, jalapeños and cheese. Topped with sour cream, pico de gallo and salsa.</p></div>
    <div class="item"><p class="name">Corvo Wings <span>$15</span></p><p class="desc">7 jumbo-size drums and flats tossed in your choice of sauce (BBQ, buffalo, mango habanero, or lemon pepper) or dry. Served with carrot and celery sticks.</p></div>
    <div class="item"><p class="name">Chicken Strips <span>$15</span></p><p class="desc">House-battered and breaded chicken breast strips. Served with fries and your choice dressing.</p></div>
    <div class="item"><p class="name">All-American Burger <span>$16</span></p><p class="desc">Verified Prairie Stock patty, cheddar cheese, with mayo, lettuce, tomato, onion and pickles.<em>- Add bacon +$3</em><em>- Add avocado +$3</em></p></div>
    <div class="item"><p class="name">Whiskey Burger <span>$17</span></p><p class="desc">Verified Prairie Stock patty, bacon, caramelized onions and Swiss cheese, with mayo and house-made Moss Haverty whiskey sauce.</p></div>
    <div class="item"><p class="name">Veggie Burger <span>$16</span></p><p class="desc">Black bean patty, with mayo, lettuce, tomato, onion, pickles and avocado.</p></div>
    <div class="item"><p class="name">Chicken Strips <span>$15</span></p><p class="desc">House-battered and breaded chicken breast strips. Served with fries and your choice dressing.</p></div>
    <div class="sides" style="margin-top:9px">
      <p class="sides-label">SIDES</p>
      <div class="sides-grid">
        <span>Basket of<br>French fries $7</span><span><br>Rice $5</span>
        <span>Beans $5</span><span>Sour cream $1</span>
        <span>Avocado $4</span><span>Guacamole $7</span>
        <span>Salsa 4oz. $2</span><span>Dressing $1</span>
      </div>
    </div>
  </div>
</section>

<section class="panel" style="left:46px;top:667px;width:222px;height:331px">
  <div class="photo nachos" role="img" aria-label="Photo of loaded nachos with sour cream and guacamole"></div>
  <div class="content" style="left:26px;top:112px;width:178px">
    <h2 class="heading center" style="line-height:1.1">SOUTH OF<br>THE BORDER</h2>
    <div class="item" style="margin-top:5px"><p class="name">3 Street Tacos <span>$12 HH $7</span></p><p class="desc">Seasoned ground beef, pork carnitas, chicken or veggies, pico de gallo and salsa. Add guac +$3</p></div>
    <div class="item"><p class="name">2-lb. Burrito <span>$15</span></p><p class="desc">Flour tortilla wrapped around your choice of meat seasoned ground beef, pork, chicken, or veggies. Rice, beans, guacamole, sour cream, salsa and Jack and cheddar cheeses.</p></div>
    <div class="item"><p class="name">Chile Colorado Burrito <span>$16</span></p><p class="desc">Special trim beef simmered in a house-made Chile Colorado sauce, rice and beans wrapped in a flour tortilla. Topped with sour cream.</p></div>
  </div>
</section>

<section class="specialties">
  <div class="content" style="left:26px;top:12px;width:212px">
    <h2 class="specialties-title">HOUSE<br>SPECIALTIES</h2>
    <p class="name" style="margin-top:4px">Pork Shank <span>$24</span></p>
    <p class="desc"><i>(Wednesdays only, until sold out)</i><br>Slow-baked pork shank (fork tender and fall-off-the-bone moist). Served with rice, beans, pico de gallo, salsa and tortillas. Ask your server about availability.</p>
  </div>
  <div class="content" style="left:257px;top:16px;width:184px">
    <p class="name">Carne Asada Entrée <span>$23</span></p>
    <p class="desc">Charbroiled skirt steak, cooked to order. Served with rice, beans, pico de gallo, salsa, sour cream, guacamole and tortillas.</p>
    <p class="name" style="margin-top:5px">Chile Colorado Entrée <span>$18</span></p>
    <p class="desc">Special trim beef simmered in a house-made Chile Colorado sauce. Served with rice, beans, sour cream and tortillas.</p>
  </div>
</section>

<section class="happy">
  <h2 class="happy-title">HAPPY HOUR</h2>
  <p style="margin-top:8px">MON- FRI</p>
  <p class="o">2-5PM &amp; 10-CLOSE</p>
  <p>ANY DRAFT BEER</p>
  <p class="o">$2 OFF</p>
  <p>SELECTED APPETIZERS</p>
  <p class="o">$5 OFF</p>
  <p>WELL DRINKS <span class="o">$2 OFF</span></p>
  <p>WINE <span class="o">$2 OFF</span></p>
</section>

<div class="daily-bar">DAILY SPECIALS 11:30 AM - 5 PM</div>

<section class="beverages">
  <div><h2 class="bev-title">BEVERAGES</h2><p class="bev" style="margin:4px 0 0 22px">Soft drinks<br>$3.50</p></div>
  <p class="bev" style="margin-top:1px">Zolta, Diet Zolta,<br>Brook Fizz,<br>Juice<br>$5</p>
  <p class="bev" style="margin:1px 0 0 8px">Orange, cranberry,<br>pineapple, grapefruit<br>Milk<br>$4</p>
</section>

<section class="days">
  <p>Margarita Monday <span>$2 off /Burgers 20%off</span></p>
  <p>Tacos Tuesday <span>$5 off /Tequila Casa Verano 1871 $19.42</span></p>
  <p>Wing Wednesday <span>$5 off / Whiskey $2 off</span></p>
  <p>Thirsty Thursday <span>Any draft beer $5/Nachos $5 off</span></p>
  <p>Emberloch Friday <span>$6 shot /Chile Colorado burrito 20%off</span></p>
  <p>Saturday and Sunday Brunch <span>10am-1pm. Mimosas and Bloody Marrys</span></p>
</section>

<p class="disclaimer">*Consuming raw or undercooked meats, poultry, seafood, shellfish, or eggs may increase your risk of foodborne illness, especially if you have certain medical conditions.</p>

</body>
</html>
```